the letter head should have the logo ( may be top left), " Larkfield Health Institute" (may be top/middle ) and the two clinics info in a vertical column ( along the left side of the page )

other physicians and official letters

• the info provided in the attachements

```html
<!DOCTYPE html>
<html lang="en">
<head>
<meta charset="utf-8">
<title>Larkfield Health Institute Letterhead</title>
<link href="https://fonts.googleapis.com/css2?family=Lato:wght@400;700&display=swap" rel="stylesheet">
<style>
  :root {
    --backdrop: #a6a6a6;
    --paper: #ffffff;
    --sidebar: #c0c0c0;
    --accent: #b0286e;
    --ink: #2c3a47;
    --body-text: #4a4a4a;
    --rule: #8f8f8f;
  }
  * { margin: 0; padding: 0; box-sizing: border-box; }
  html, body {
    width: 1200px; height: 1200px; overflow: hidden;
    background: var(--backdrop);
    font-family: "Lato", Arial, sans-serif;
  }
  .letterhead {
    position: absolute; left: 175px; top: 51px;
    width: 849px; height: 1098px;
    background: var(--paper);
    display: flex;
  }
  .contact-column {
    width: 180px; height: 100%;
    background: var(--sidebar);
    position: relative;
  }
  .offices {
    position: absolute; left: 32px; bottom: 34px; width: 128px;
  }
  .office-name {
    color: var(--accent); font-weight: 700; font-size: 12.5px;
    margin-bottom: 6px;
  }
  .office-line {
    display: flex; align-items: flex-start; gap: 5px;
    font-size: 10.5px; line-height: 13px; color: var(--body-text);
  }
  .office-line svg { flex: none; width: 8px; height: 8px; margin-top: 2.5px; fill: var(--accent); }
  .office-line.address { margin-top: 4px; }
  .office-divider {
    border: 0; border-top: 1px solid var(--rule);
    margin: 8px 0 13px; width: 116px;
  }
  .brand {
    position: absolute; left: 594px; top: 54px; width: 176px;
  }
  .brand-row { display: flex; align-items: center; gap: 8px; }
  .brand-mark { width: 58px; height: 78px; background: var(--ink); flex: none; }
  .brand-name {
    color: var(--ink); font-size: 22px; line-height: 26px; font-weight: 400;
  }
  .brand-tagline {
    margin-top: 4px; padding-top: 2px;
    border-top: 1px solid var(--ink);
    color: var(--accent); font-size: 9.5px; letter-spacing: 0.1px;
    white-space: nowrap;
  }
</style>
</head>
<body>
  <div class="letterhead">
    <aside class="contact-column">
      <div class="offices">
        <section class="office">
          <h2 class="office-name">Northgate Office</h2>
          <p class="office-line"><svg viewBox="0 0 10 10"><path d="M2 0.5l2 2-1 1.3c.6 1.3 1.6 2.3 2.9 2.9l1.3-1 2 2-1.2 1.8C4.8 9.3.7 5.2.2 1.7z"/></svg>555-014-7390</p>
          <p class="office-line"><svg viewBox="0 0 10 10"><path d="M2 0h5v3H2zM0 3.5h10V9H0zM2 6h6v1H2z"/></svg>555-014-8152</p>
          <p class="office-line address"><svg viewBox="0 0 10 10"><path d="M5 0a3.5 3.5 0 0 1 3.5 3.5C8.5 6 5 10 5 10S1.5 6 1.5 3.5A3.5 3.5 0 0 1 5 0zm0 2a1.4 1.4 0 1 0 0 2.8A1.4 1.4 0 0 0 5 2z"/></svg><span>210 S. Harbor Ave.<br>Suite 207, 40215</span></p>
        </section>
        <hr class="office-divider">
        <section class="office">
          <h2 class="office-name">Riverside Office</h2>
          <p class="office-line"><svg viewBox="0 0 10 10"><path d="M2 0.5l2 2-1 1.3c.6 1.3 1.6 2.3 2.9 2.9l1.3-1 2 2-1.2 1.8C4.8 9.3.7 5.2.2 1.7z"/></svg>555-019-6023</p>
          <p class="office-line"><svg viewBox="0 0 10 10"><path d="M2 0h5v3H2zM0 3.5h10V9H0zM2 6h6v1H2z"/></svg>555-019-3470</p>
          <p class="office-line address"><svg viewBox="0 0 10 10"><path d="M5 0a3.5 3.5 0 0 1 3.5 3.5C8.5 6 5 10 5 10S1.5 6 1.5 3.5A3.5 3.5 0 0 1 5 0zm0 2a1.4 1.4 0 1 0 0 2.8A1.4 1.4 0 0 0 5 2z"/></svg><span>4820 S. Linden St.<br>Riverside 40617</span></p>
        </section>
      </div>
    </aside>
    <header class="brand">
      <div class="brand-row">
        <span class="brand-mark"></span>
        <h1 class="brand-name">Larkfield Health Institute</h1>
      </div>
      <p class="brand-tagline">where steady care meets new science</p>
    </header>
  </div>
</body>
</html>
```